Tree Service Billboard 20x8 ft

We need a billboard design for a tree service company.
The billboard is 20ft x 8 ft so we need a design that is capable to stretching to those dimensions without loosing quality.
I have attached a series of images.
Image 1- Simply a billboard that I think looks good that I would like you to use for inspiration. I am aiming for the same format only no color in the wording, just black white, or gray. I like the the trees in the background, the logo placed to the left, and wording on the right.
Image 2- Current Logo I would like to the left of the billboard
Image 3- Another format of current logo if needed.
Image 4- A drawn out design template
Image 5- Another drawn out design template

Specific things I am looking for
-The contact number to be the largest thing on the design
-The logo on the design
-Key points to the design to say:
Tree Removal
Tree Trimming
Land Development
Stump Grinding
Storm Response
Insured
Free Bids
-The facebook logo
-The Google Logo

```html
<!DOCTYPE html>
<html lang="en">
<head>
<meta charset="utf-8">
<title>Birch Line Tree Care – Billboard</title>
<link href="https://fonts.googleapis.com/css2?family=Alegreya+Sans+SC:wght@700;800&display=swap" rel="stylesheet">
<style>
  :root {
    --page: #e9ece8;
    --leaf-light: #4f8a2e;
    --leaf-mid: #2f5e1f;
    --leaf-dark: #16301a;
    --panel: #050505;
    --white: #ffffff;
    --grey: #5c5c5c;
    --ring: #1a1a1a;
    --social-circle: #1877f2;
    --social-square: #f4f4f4;
  }
  html, body {
    margin: 0;
    padding: 0;
    width: 1200px;
    height: 879px;
    overflow: hidden;
    background: var(--page);
  }
  .billboard {
    position: absolute;
    left: 0;
    top: 211px;
    width: 1200px;
    height: 457px;
    overflow: hidden;
    font-family: "Alegreya Sans SC", "Arial Narrow", sans-serif;
    font-weight: 800;
  }
  .canopy-photo {
    position: absolute;
    inset: 0;
    background:
      radial-gradient(ellipse at 50% 20%, rgba(170,190,160,0.35), transparent 40%),
      radial-gradient(ellipse at 20% 60%, var(--leaf-light), transparent 55%),
      radial-gradient(ellipse at 80% 40%, var(--leaf-light), transparent 55%),
      linear-gradient(180deg, var(--leaf-mid), var(--leaf-dark));
  }
  .brand {
    position: absolute;
    left: 40px;
    top: 50px;
    width: 380px;
    text-align: center;
  }
  .brand-mark {
    display: block;
    margin: 0 auto;
    width: 172px;
    height: 172px;
    border-radius: 50%;
    border: 6px solid var(--ring);
    background: var(--white);
    box-sizing: border-box;
  }
  .brand-name {
    margin: 10px 0 0;
    font-size: 44px;
    line-height: 1;
    color: var(--white);
    letter-spacing: 0.5px;
  }
  .brand-phone {
    margin: 8px 0 0;
    font-size: 30px;
    line-height: 1;
    color: var(--white);
    display: flex;
    align-items: center;
    justify-content: center;
    gap: 12px;
  }
  .brand-phone::before,
  .brand-phone::after {
    content: "";
    width: 50px;
    height: 3px;
    background: var(--white);
  }
  .services {
    position: absolute;
    left: 436px;
    top: 100px;
    display: grid;
    grid-template-columns: 364px 366px;
    column-gap: 14px;
    row-gap: 7px;
    margin: 0;
    padding: 0;
    list-style: none;
  }
  .service {
    height: 55px;
    background: var(--panel);
    color: var(--white);
    font-size: 40px;
    line-height: 55px;
    text-align: center;
  }
  .service:nth-child(2n) { grid-column: 2; }
  .service:nth-child(2n+1) { grid-column: 1; }
  .insured {
    position: absolute;
    left: 125px;
    top: 368px;
    width: 180px;
    text-align: center;
    color: var(--white);
    font-size: 38px;
    line-height: 45px;
    margin: 0;
  }
  .social {
    position: absolute;
    left: 1015px;
    top: 396px;
    display: flex;
    gap: 14px;
  }
  .social-circle {
    width: 56px;
    height: 56px;
    border-radius: 50%;
    background: var(--social-circle);
  }
  .social-square {
    width: 57px;
    height: 57px;
    background: var(--social-square);
  }
</style>
</head>
<body>
  <section class="billboard" aria-label="Birch Line Tree Care billboard">
    <div class="canopy-photo" role="img" aria-label="Photo looking up into a green tree canopy with dark branches"></div>

    <div class="brand">
      <span class="brand-mark" aria-hidden="true"></span>
      <p class="brand-name">Birch Line Tree Care</p>
      <p class="brand-phone">555-014-2290</p>
    </div>

    <ul class="services">
      <li class="service">Tree Removal</li>
      <li class="service">Stump Grinding</li>
      <li class="service">Tree Trimming</li>
      <li class="service">Storm Response</li>
      <li class="service">Land Development</li>
      <li class="service">Free Bids</li>
    </ul>

    <p class="insured">Fully<br>Insured</p>

    <div class="social" aria-label="Social profiles">
      <span class="social-circle"></span>
      <span class="social-square"></span>
    </div>
  </section>
</body>
</html>
```